Varolta Business Card

I am looking for a business card design for a start-up company called Varolta Group. This is a management consultancy focused on sales, marketing, sales management, product management and AGILE software development. Our primary customers are $1M to $50M in revenue.

Varolta is the Italian word for "slope."

The path from $0 to $50M has many different growth stages associated with it. Each one having a significant slope to the next plateau. Our expertise helps our customers ascend each of those slopes. We bring experience, successful track-records in growing companies, best practices and a dive-in and roll-up your sleeves mentality. We are not sitting at base camp shouting instructions, we are right there with you, on the climb.

Industry/Entity Type

Business

```html
<!DOCTYPE html>
<html lang="en">
<head>
<meta charset="utf-8">
<title>Varolta Business Card</title>
<link rel="stylesheet" href="https://fonts.googleapis.com/css2?family=Source+Sans+3:wght@400;600&display=swap">
<style>
  :root {
    --page: #ffffff;
    --card-dark: #1c1c1d;
    --card-mid: #3a3a3c;
    --silver-light: #f4f4f4;
    --silver-dark: #a9a9ab;
    --ring: #2b2b2d;
    --green: #7fb241;
    --green-dark: #4e8a26;
    --brand-grey: #9aa3ad;
    --mark: #4a6f9c;
    --white: #ffffff;
  }
  * { margin: 0; padding: 0; box-sizing: border-box; }
  html, body {
    width: 1200px; height: 1084px; overflow: hidden;
    background: var(--page);
    font-family: "Source Sans 3", sans-serif;
  }
  .canvas { position: relative; width: 1200px; height: 1084px; }
  .card {
    position: absolute;
    border-radius: 24px;
    overflow: hidden;
    background: radial-gradient(circle at 30% 35%, var(--card-mid), var(--card-dark) 70%);
  }
  .card--front { left: 42px; top: 42px; width: 762px; height: 432px; }
  .card--back { left: 342px; top: 612px; width: 762px; height: 426px; }
  .card__art { position: absolute; inset: 0; }

  .holder { position: absolute; left: 48px; top: 120px; width: 300px; text-align: center; }
  .holder__name { color: var(--white); font-size: 42px; font-weight: 400; line-height: 1.1; white-space: nowrap; }
  .holder__title { color: var(--green); font-size: 28px; line-height: 1.3; }

  .contact-pill {
    position: absolute; left: 0; height: 48px;
    border-radius: 0 24px 24px 0;
    background: linear-gradient(to bottom, var(--green), var(--green-dark));
    color: var(--white); font-size: 28px; line-height: 48px;
    padding-left: 40px;
  }
  .contact-pill--email { top: 282px; width: 318px; }
  .contact-pill--phone { top: 354px; width: 378px; padding-left: 96px; }

  .brand-name {
    position: absolute; color: var(--brand-grey);
    font-size: 80px; font-weight: 400; line-height: 1; letter-spacing: -1px;
  }
  .card--front .brand-name { right: 28px; bottom: 22px; }
  .card--back .brand-name {
    left: 110px; top: 26px;
    transform-origin: left top; transform: rotate(90deg);
  }
  .web-address {
    position: absolute; right: 30px; bottom: 14px;
    color: var(--green); font-size: 28px;
  }
</style>
</head>
<body>
<div class="canvas">

  <section class="card card--front">
    <svg class="card__art" width="762" height="432" viewBox="0 0 762 432" aria-hidden="true">
      <defs>
        <linearGradient id="silver-front" x1="0" y1="0" x2="1" y2="0">
          <stop offset="0" stop-color="var(--silver-light)"/>
          <stop offset="1" stop-color="var(--silver-dark)"/>
        </linearGradient>
      </defs>
      <circle cx="600" cy="174" r="210" fill="var(--ring)"/>
      <path d="M612 18 H762 V330 H612 A156 156 0 0 1 612 18 Z" fill="url(#silver-front)"/>
      <circle cx="612" cy="174" r="140" fill="var(--mark)"/>
    </svg>
    <div class="holder">
      <p class="holder__name">Marco Delvane</p>
      <p class="holder__title">President</p>
    </div>
    <p class="contact-pill contact-pill--email">marco@varolta.com</p>
    <p class="contact-pill contact-pill--phone">555.214.7308</p>
    <p class="brand-name">Varolta</p>
  </section>

  <section class="card card--back">
    <svg class="card__art" width="762" height="426" viewBox="0 0 762 426" aria-hidden="true">
      <defs>
        <linearGradient id="silver-back" x1="0" y1="0" x2="1" y2="0">
          <stop offset="0" stop-color="var(--silver-light)"/>
          <stop offset="1" stop-color="var(--silver-dark)"/>
        </linearGradient>
      </defs>
      <circle cx="370" cy="190" r="230" fill="var(--ring)"/>
      <path d="M378 12 H762 V360 H378 A174 174 0 0 1 378 12 Z" fill="url(#silver-back)"/>
      <circle cx="378" cy="186" r="160" fill="var(--mark)"/>
    </svg>
    <p class="brand-name">Varolta</p>
    <p class="web-address">www.varolta.com</p>
  </section>

</div>
</body>
</html>
```